Design nice user interface for an IQ test website

I need you to design a modern user interface for IQ-test website. Questions and answers for the test are already known.

The test itself has all the questions in the form of an image where a portion of the image is cut off, and then the user has either 6 or 8 possible answers. The user needs to click one option to select his answer.

Proof of concept is here (you can find test questions there already):
https://quenbrit.org/projects/IQ-test/

I need only the design from you, no programming at all. The test questions are already given, you will not create your own questions/answers. Note that the images for test questions and answers (as shown at the URL) are not blue, they are transparent PNGs. So the background does not need to be blue.

While thinking about the design, consider adding nice progress bar (so user knows how many more questions to answer), and there needs to be also a time limit, which counts from 40:00 minutes down to zero.

Redesign for the actual questions/answer images is not required. If you decide to redesign the questions to make them nicer, you can do so, you may have higher chances to be selected as a winner, but keep in mind there are 60 questions in total, so it will be lot of additional work for you (feel free to suggest your idea).

Keep in mind that the design must be convertable to a "portrait mode" (eg. for devices where screen width is small)

Feel free to get as creative as you like.

So basically I would like to see at least 3 pages from you designed:
- some basic main page of the website with some lorem ipsum texts, and a "START TEST" button
- test page (where the test questions are displayed and answers are selected)
- a form page (after test is completed, user will enter name/email/age and click some button to get the test results emailed to him)

```html
<!DOCTYPE html>
<html lang="en">
<head>
<meta charset="UTF-8">
<title>IQ Test – Welcome</title>
<link href="https://fonts.googleapis.com/css2?family=Plus+Jakarta+Sans:wght@400;500;700;800&display=swap" rel="stylesheet">
<style>
  :root {
    --header-blue: #1f6cf3;
    --page-blue: #3a7ef9;
    --art-light: #5f97fb;
    --art-deep: #2e6fe8;
    --yellow: #ffc800;
    --yellow-shade: #e3a900;
    --white: #ffffff;
    --footer-bg: #eff3fa;
    --footer-text: #1f2430;
  }
  * { box-sizing: border-box; margin: 0; padding: 0; }
  html, body {
    width: 1200px;
    height: 2784px;
    overflow: hidden;
    font-family: "Plus Jakarta Sans", sans-serif;
    background: var(--page-blue);
  }
  .site-header {
    position: absolute; left: 0; top: 0;
    width: 1200px; height: 230px;
    background: var(--header-blue);
  }
  .brand {
    position: absolute; left: 77px; top: 60px;
    color: var(--white);
    font-weight: 700;
    font-size: 56px;
    line-height: 54px;
    letter-spacing: 1px;
  }
  .menu-toggle {
    position: absolute; left: 1034px; top: 86px;
    width: 76px; height: 58px;
  }
  .hero {
    position: absolute; left: 0; top: 230px;
    width: 1200px; height: 2372px;
    background: var(--page-blue);
  }
  .hero-art {
    position: absolute; left: 184px; top: 266px;
    width: 832px; height: 808px;
    border-radius: 24px;
    background: radial-gradient(ellipse at 50% 45%, var(--art-light) 0%, var(--page-blue) 75%);
  }
  .hero-title {
    position: absolute; left: 74px; top: 1290px;
    color: var(--white);
    font-weight: 700;
    font-size: 113px;
    letter-spacing: -3px;
    white-space: nowrap;
  }
  .hero-text {
    position: absolute; left: 77px; top: 1470px;
    width: 1060px;
    color: var(--white);
    font-weight: 400;
    font-size: 41px;
    line-height: 70px;
    letter-spacing: -0.6px;
  }
  .start-button {
    position: absolute; left: 77px; top: 1781px;
    width: 1046px; height: 151px;
    background: var(--yellow);
    border-radius: 10px;
    box-shadow: inset 0 -13px 0 var(--yellow-shade);
    display: flex; align-items: center; justify-content: center;
    gap: 30px;
    color: var(--white);
    font-weight: 700;
    font-size: 41px;
    letter-spacing: 0;
    padding-bottom: 8px;
  }
  .site-footer {
    position: absolute; left: 0; top: 2602px;
    width: 1200px; height: 182px;
    background: var(--footer-bg);
    display: flex; align-items: center; justify-content: center;
    color: var(--footer-text);
    font-size: 41px;
    font-weight: 400;
    letter-spacing: -0.5px;
  }
</style>
</head>
<body>
  <header class="site-header">
    <div class="brand">YOUR<br>LOGO</div>
    <svg class="menu-toggle" viewBox="0 0 76 58" aria-label="Menu">
      <rect x="0" y="0" width="76" height="6" fill="#fff"/>
      <rect x="0" y="26" width="76" height="6" fill="#fff"/>
      <rect x="0" y="52" width="76" height="6" fill="#fff"/>
    </svg>
  </header>

  <main class="hero">
    <div class="hero-art" role="img" aria-label="Illustration of two people at a desk with a laptop and tablet, a green light bulb above them"></div>
    <h1 class="hero-title">Welcome to IQ Test</h1>
    <p class="hero-text">Lorem ipsum dolor sit amet, consectetur adipis elit. Nisl massa in tincidunt viverra tristique a faucibus elit. Est leo mauris diam quam sit. Quam.</p>
    <a class="start-button">
      <svg width="38" height="40" viewBox="0 0 38 40" aria-hidden="true"><path d="M0 0 L38 20 L0 40 Z" fill="#fff"/></svg>
      START IQ TEST
    </a>
  </main>

  <footer class="site-footer">Copyright @YourBrand All Right Reserved</footer>
</body>
</html>
```